A Label for an ECO Friendly Spirit Company

Design a label which can be used for vodka and gin (London Dry Gin). It should be Square type Like the Shape File you see in the uploads. VORK means Local Eco friendly Authentic and Fair. We want a cool and slim label that calls for eco-friendly. We want to use it for our premium
Vodka and our London Dry Gin. Please use the logo and design it in Square Type.

40%vol, 700ml

Target Market(s)

spirits and events

Industry/Entity Type

SPIRITS

Colors
00AB8E
00BBA5
67D7C9
C6EFE9
E9F9F6
59FF00
82FF00
B8FF75
E3FFCB
F4FFEA

Requirements
Must have
• Logo from VORK, Squaee Shape

```html
<!DOCTYPE html>
<html lang="en">
<head>
<meta charset="utf-8">
<title>VORK London Dry Gin – Label</title>
<link rel="stylesheet" href="https://fonts.googleapis.com/css2?family=Montserrat:wght@500;600;700&family=Oswald:wght@500&display=swap">
<style>
  :root {
    --copper: #c17f47;
    --teal: #3aa98b;
    --teal-soft: #8fd3c0;
    --mint: #e9f7f2;
    --ink: #0d3a4a;
    --paper: #ffffff;
  }
  html, body {
    margin: 0;
    width: 1200px;
    height: 659px;
    overflow: hidden;
    background: var(--paper);
  }
  .label {
    display: block;
    width: 1200px;
    height: 659px;
  }
  .frame-outer { fill: var(--paper); stroke: var(--copper); stroke-width: 6; }
  .frame-inner { fill: none; stroke: var(--teal); stroke-width: 2; }
  .band-rule { stroke: var(--copper); stroke-width: 4; }
  .deco-line { fill: none; stroke: var(--teal); stroke-width: 1.6; }
  .brand-mark { fill: var(--teal); }
  .brand-name { font-family: "Montserrat", sans-serif; font-weight: 600; font-size: 24px; fill: var(--teal); }
  .style-name { font-family: "Montserrat", sans-serif; font-weight: 700; font-size: 17px; letter-spacing: 6px; fill: var(--ink); }
  .product-name { font-family: "Oswald", sans-serif; font-weight: 500; font-size: 190px; fill: var(--ink); }
  .tagline { font-family: "Montserrat", sans-serif; font-weight: 700; font-size: 17px; letter-spacing: 4px; fill: var(--copper); }
  .spec { font-family: "Montserrat", sans-serif; font-weight: 500; font-size: 12.5px; letter-spacing: 1px; fill: var(--ink); }
</style>
</head>
<body>
<svg class="label" viewBox="0 0 1200 659" xmlns="http://www.w3.org/2000/svg">
  <defs>
    <linearGradient id="foliage" x1="0" y1="0" x2="1" y2="0">
      <stop offset="0" stop-color="#f6fcfa"/>
      <stop offset="0.5" stop-color="#cfeee4"/>
      <stop offset="1" stop-color="#f6fcfa"/>
    </linearGradient>
  </defs>

  <!-- outer frame -->
  <polygon class="frame-outer" points="600,30 900,330 600,630 300,330"/>
  <polygon class="frame-inner" points="600,46 884,330 600,614 316,330"/>

  <!-- top and bottom line-pattern panels -->
  <polygon role="img" aria-label="Fine teal art deco line pattern with copper dot accents" fill="var(--mint)" points="600,52 785,236 415,236"/>
  <polygon role="img" aria-label="Fine teal art deco line pattern with copper dot accents" fill="var(--mint)" points="600,608 785,424 415,424"/>

  <!-- inner deco lines -->
  <polyline class="deco-line" points="470,236 600,106 730,236"/>
  <polyline class="deco-line" points="470,424 600,554 730,424"/>

  <!-- central band -->
  <polygon role="img" aria-label="Teal botanical leaves and vines illustration" fill="url(#foliage)" points="400,246 800,246 884,330 800,414 400,414 316,330"/>
  <polygon class="frame-inner" points="410,246 790,246 872,330 790,414 410,414 328,330"/>
  <line class="band-rule" x1="394" y1="241" x2="806" y2="241"/>
  <line class="band-rule" x1="394" y1="419" x2="806" y2="419"/>

  <!-- brand -->
  <rect class="brand-mark" x="553" y="176" width="18" height="18" rx="3"/>
  <text class="brand-name" x="578" y="194">VORK</text>

  <text class="style-name" x="600" y="230" text-anchor="middle">LONDON DRY</text>

  <text class="product-name" x="514" y="402" textLength="172" lengthAdjust="spacingAndGlyphs">GIN</text>

  <text class="tagline" x="600" y="448" text-anchor="middle">PREMIUM SPIRIT</text>
  <text class="spec" x="600" y="481" text-anchor="middle">40% VOL</text>
  <text class="spec" x="600" y="499" text-anchor="middle">700ML</text>
</svg>
</body>
</html>
```